Short-Term Rental Website - Management Services for Property Owner

We are looking for a website to advertise our short-term rental business, Bright Door Rental Management, currently www.brightdoorstays.ca. Hosted on WordPress.

We have the website main page language but we are looking for someone who is creative and can present the information in a trendy, cool and professional way. I like the closed design crowd job "Plumwick Media - SEM, Influencer website. FUN RETRO VIBES" (see attached pictures) in terms of how the page flows, icons and stock images, other connective imagery and design features

Our main competitor website is www.hostvela.com and we like how that website feels but we like the elegance of www.Torvane-Alsky.com (desktop) and main page of www.quorrin.ca (desktop version). We like the slow type video on quorrin.com.

MUST LOOK GOOD ON MOBILE. The mobile experience has to be good.

The content in terms of the language is in one of the attached files.

Our landing page requires the following sections;
- Revenue Maximization
- Services (I have included the content that we want highlighted but we are looking for someone to be creative with how these are displayed
- Pricing
- Featured Properties (display on a carousel) *must design a carousel that can be easily populated.
- Reviews (display on a carousel) *must design a carousel that can be easily populated.
- Contact Us (first name, last name, email, phone (required), description of property)

The header will have;
- Logo (link to main page)
- Pricing (link to pricing section found on the main page)
- Services (link to services section found on the main page)
- Properties (separate page)
- Contact (link to contact area on main page)

We would also need a coded template page that we could use to add additional pages as needed.

For the properties page, we need a landing page that would allow our guests to see all of our properties and a map view with the properties plotted on the map.

As we would collect personal information we would need a cookies/ privacy policy.

The colour palette should be on the light side. We do not want the website to have a dark feel. Colours should be consistent with that of our logo but we are open to creativity.

Investment property owners

Real Estate

2 page

Sans Serif

• Very strong and well designed landing page

Second page which showcases properttes

Template property page that can be easily reproduced

```html
<!DOCTYPE html>
<html lang="en">
<head>
<meta charset="utf-8">
<title>Bright Door Rental Management</title>
<link href="https://fonts.googleapis.com/css2?family=Poppins:wght@300;400;500;600;700&display=swap" rel="stylesheet">
<style>
:root{
  --teal:#4f7f8c;
  --teal-dark:#3f6c78;
  --navy:#3b4352;
  --ink:#2f3440;
  --body:#6b6f78;
  --soft:#eef3f5;
  --line:#d9dee2;
  --white:#ffffff;
}
*{box-sizing:border-box;margin:0;padding:0}
html,body{width:1200px;height:5333px;overflow:hidden}
body{font-family:'Poppins',sans-serif;color:var(--body);background:var(--white);position:relative}
.abs{position:absolute}
h1,h2,h3{color:var(--ink);font-weight:600}

/* header */
.site-header{position:absolute;top:0;left:0;width:1200px;height:92px;background:var(--white);z-index:5}
.brand{position:absolute;left:88px;top:24px;display:flex;align-items:center;gap:10px}
.brand-mark{width:34px;height:34px;background:var(--teal);border-radius:4px}
.brand-name{font-size:30px;font-weight:700;color:var(--teal);line-height:1}
.brand-sub{font-size:8px;letter-spacing:2px;color:var(--navy);font-weight:600;display:block;margin-top:2px}
.nav{position:absolute;right:70px;top:28px;display:flex;align-items:center;gap:36px;font-size:13px;font-weight:500;color:var(--ink)}
.nav .active{color:var(--teal)}
.nav .pill{border:2px solid var(--ink);border-radius:20px;padding:6px 20px;font-size:12px}

/* hero */
.hero{position:absolute;top:92px;left:0;width:1200px;height:760px;overflow:hidden}
.hero-photo{position:absolute;inset:0;background:linear-gradient(110deg,#7c8cae 0%,#99a8c4 40%,#c9d1de 62%,#8e9bb0 80%,#6b7993 100%)}
.hero-cut{position:absolute;left:0;bottom:0}
.hero-line{position:absolute;left:88px;top:178px;width:2px;height:330px;background:rgba(255,255,255,.7)}
.hero-title{position:absolute;left:120px;top:195px;color:var(--white);font-size:92px;font-weight:700;line-height:.98}
.hero-sub{position:absolute;left:120px;top:385px;width:430px;color:var(--white);font-size:22px;font-weight:500;line-height:1.35}

/* features */
.feature{position:absolute;top:900px;width:350px;height:365px;text-align:center;padding:32px 38px 0}
.feature.raised{background:var(--white);box-shadow:0 10px 30px rgba(0,0,0,.12);border-bottom:4px solid var(--teal)}
.feature svg{width:90px;height:90px}
.feature h3{font-size:21px;line-height:1.3;margin:12px 0 22px}
.feature p{font-size:12.5px;line-height:1.6}

/* services */
.section-title{position:absolute;left:0;width:1200px;text-align:center;font-size:42px;font-weight:600;color:var(--ink)}
.svc{position:absolute;width:390px;display:flex;align-items:center;gap:18px}
.svc.left{left:30px;justify-content:flex-end;text-align:right}
.svc.right{left:780px}
.svc-icon{width:76px;height:76px;background:var(--soft);flex:none;display:flex;align-items:center;justify-content:center}
.svc-icon svg{width:44px;height:44px}
.svc h4{font-size:18px;font-weight:500;color:var(--ink);margin-bottom:8px}
.svc p{font-size:13px;line-height:1.5}
.emblem{position:absolute;left:450px;top:1460px;width:300px;height:270px;border-radius:50%;background:radial-gradient(circle,#6f99a4 0%,#4f7f8c 70%)}
.btn-outline{position:absolute;left:512px;top:1793px;width:176px;height:40px;border:2px solid var(--ink);border-radius:22px;font-size:12.5px;font-weight:500;color:var(--ink);display:flex;align-items:center;justify-content:center;letter-spacing:.5px}

/* fee */
.fee-band{position:absolute;top:1918px;left:0}
.fee-strip{position:absolute;left:0;top:1918px;width:85px;height:450px;background:var(--navy);overflow:hidden}
.fee-strip span{position:absolute;left:20px;top:400px;transform:rotate(-90deg);transform-origin:left top;font-size:62px;font-weight:700;color:rgba(255,255,255,.07);white-space:nowrap}
.fee-title{position:absolute;left:145px;top:2012px;width:380px;color:var(--white);font-size:40px;font-weight:600;line-height:1}
.fee-text{position:absolute;left:145px;top:2150px;width:350px;color:var(--white);font-size:12.5px;line-height:1.6}
.fee-table{position:absolute;left:550px;top:2068px;width:570px;height:245px;background:var(--white);box-shadow:0 12px 30px rgba(0,0,0,.15);border-collapse:collapse;font-size:12.5px;color:var(--ink)}
.fee-table th{text-align:left;font-weight:600;padding:14px 10px;vertical-align:top;border-bottom:1px solid var(--line)}
.fee-table td{padding:10px;border:1px solid var(--line);vertical-align:middle}
.fee-table tr:last-child td{border-top:2px solid var(--teal);color:var(--teal);font-weight:600}

/* str / overview */
.photo{position:absolute}
.photo div{width:100%;height:100%}
.block-title{position:absolute;font-size:40px;font-weight:600;color:var(--ink);line-height:1.05}
.block-text{position:absolute;font-size:13px;line-height:1.6}
.block-text p{margin-bottom:14px}

/* pricing */
.pricing-bg{position:absolute;left:0;top:3570px;width:1200px;height:650px;background:var(--soft)}
.price-card{position:absolute;left:204px;top:3745px;width:794px;height:440px;background:var(--white);box-shadow:0 10px 30px rgba(0,0,0,.08);display:flex}
.price-side{flex:0 0 298px;width:298px;background:var(--teal);color:var(--white);padding:40px 34px;font-size:16px;line-height:1.45}
.price-side .lead-side{font-weight:600;font-size:17px;line-height:1.4}
.price-side .big{font-size:62px;font-weight:700;margin:24px 0 20px;line-height:1}
.price-side strong{font-weight:600}
.price-side p{margin-bottom:20px}
.price-main{flex:1;padding:40px 48px;font-size:17px;line-height:1.5}
.price-main .lead{font-weight:500;color:var(--ink);margin-bottom:30px}
.price-main p{margin-bottom:28px}
.btn-dark{display:inline-block;background:var(--navy);color:var(--white);border-radius:28px;padding:16px 30px;font-size:13px;font-weight:500;letter-spacing:.5px}

/* contact */
.contact-title{position:absolute;left:88px;top:4385px;width:450px;font-size:40px;font-weight:600;color:var(--ink);line-height:1.1}
.field{position:absolute}
.field label{display:block;font-size:11px;font-weight:600;color:var(--ink);margin-bottom:8px}
.field .box{background:#eff1f3;height:46px;padding:14px 16px;font-size:13px;color:#9aa0a8}
.btn-submit{position:absolute;left:793px;top:4665px;width:156px;height:42px;background:var(--teal);color:var(--white);border-radius:22px;font-size:13px;font-weight:600;display:flex;align-items:center;justify-content:center}

/* footer */
.footer-bg{position:absolute;left:0;top:4700px}
.news-title{position:absolute;left:0;width:1200px;top:4860px;text-align:center;color:var(--white);font-size:40px;font-weight:600}
.news-form{position:absolute;left:277px;top:4935px;width:648px;height:60px;background:var(--white);border-radius:30px;display:flex;align-items:center;padding:0 8px 0 28px;font-size:15px;color:var(--body)}
.news-form .mail{width:16px;height:12px;background:#b8c2cc;margin-right:10px}
.news-form .go{margin-left:auto;background:var(--teal);color:var(--white);border-radius:24px;padding:12px 34px;font-size:14px;font-weight:600}
.foot-brand{position:absolute;left:88px;top:5070px;display:flex;align-items:center;gap:12px}
.foot-brand .brand-name{font-size:42px}
.foot-brand .brand-sub{color:var(--white)}
.social{position:absolute;left:152px;top:5152px;display:flex;gap:12px}
.social span{width:34px;height:34px;border-radius:50%;background:var(--teal)}
.foot-col{position:absolute;top:5030px;color:var(--white);font-size:13px;line-height:2}
.foot-col h5{font-size:18px;font-weight:500;color:#7f8a9a;margin-bottom:12px}
.contact-row{display:flex;align-items:flex-start;gap:12px;line-height:1.4;margin-bottom:16px}
.contact-row svg{flex:none;margin-top:2px}
.copy{position:absolute;left:0;width:1200px;top:5283px;text-align:center;color:var(--white);font-size:13px}
.chat{position:absolute;left:1132px;top:5238px;width:40px;height:40px;border-radius:50%;background:var(--white);display:flex;align-items:center;justify-content:center}
</style>
</head>
<body>

<header class="site-header">
  <div class="brand">
    <span class="brand-mark"></span>
    <div><span class="brand-name">BrightDoor</span><span class="brand-sub">Rental Management</span></div>
  </div>
  <nav class="nav">
    <span class="active">HOME</span><span>PRICING</span><span>SERVICES</span><span>PROPERTIES</span>
    <span class="pill">CONTACT US</span>
    <svg width="16" height="16" viewBox="0 0 16 16"><circle cx="7" cy="7" r="5" fill="none" stroke="#2f3440" stroke-width="2"/><path d="M11 11l4 4" stroke="#2f3440" stroke-width="2"/></svg>
  </nav>
</header>

<section class="hero">
  <div class="hero-photo" role="img" aria-label="Modern glass residential tower against a cloudy sky"></div>
  <svg class="hero-cut" width="1200" height="760" viewBox="0 0 1200 760">
    <polygon points="0,760 1200,420 1200,760" fill="#4f7f8c"/>
    <polygon points="0,760 1200,540 1200,760" fill="#ffffff"/>
  </svg>
  <div class="hero-line"></div>
  <h1 class="hero-title">Your<br>Property's</h1>
  <p class="hero-sub">Value will be optimized to reach its potential through our revenue maximization services</p>
</section>

<article class="feature" style="left:63px">
  <svg viewBox="0 0 90 90" fill="none" stroke="#3b4352" stroke-width="2"><circle cx="40" cy="38" r="22"/><text x="40" y="42" font-size="10" font-family="Poppins,sans-serif" text-anchor="middle" fill="#3b4352" stroke="none">SEO</text><circle cx="55" cy="62" r="9"/><path d="M61 69l10 10"/></svg>
  <h3>Staynest Search Engine Optimization</h3>
  <p>Staynest ranks all listings using an algorithm (much like Searchly) and our optimization techniques allow your listing to appear higher in search results and receive more bookings.</p>
</article>
<article class="feature raised" style="left:425px">
  <svg viewBox="0 0 90 90" fill="none" stroke="#3b4352" stroke-width="2"><rect x="18" y="12" width="48" height="64"/><rect x="30" y="7" width="24" height="9"/><path d="M26 30h8M40 30h18M26 44h8M40 44h18M26 58h8M40 58h10"/><circle cx="64" cy="68" r="10"/><path d="M64 62v6h5"/></svg>
  <h3>Proprietary Pricing Tool</h3>
  <p>We have developed a proprietary pricing tool that allows us to determine future nightly rates based on demand. This tool has led us to managing the #1 &amp; #5 Highest Revenue 2-Bedroom Listings in Calgary.</p>
</article>
<article class="feature" style="left:787px">
  <svg viewBox="0 0 90 90" fill="none" stroke="#3b4352" stroke-width="2"><rect x="12" y="16" width="60" height="54"/><path d="M12 28h60M22 10v10M34 10v10M46 10v10M58 10v10"/><path d="M22 40h4M34 40h4M46 40h4M22 52h4M34 52h4"/><circle cx="64" cy="64" r="12" fill="#fff"/><path d="M58 64l4 4 8-8"/></svg>
  <h3>Strategic Calendar Management</h3>
  <p>Our strategy focuses on future bookings being as long as possible. This, along with other techniques, has resulted in our properties averaging an ~85% occupancy rate which is ~20% above market average.</p>
</article>

<h2 class="section-title" style="top:1365px">Our Services</h2>
<div class="emblem" role="img" aria-label="Brand emblem"></div>

<div class="svc left" style="top:1433px"><div><h4>Guest Experience</h4><p>End-to-end management of<br>the guest experience</p></div><div class="svc-icon"><svg viewBox="0 0 44 44" fill="none" stroke="#3b4352" stroke-width="1.6"><circle cx="16" cy="15" r="5"/><path d="M6 32c0-6 4-10 10-10s10 4 10 10"/><circle cx="31" cy="28" r="7"/><path d="M28 28l2 2 4-4"/></svg></div></div>
<div class="svc left" style="top:1563px"><div><h4>Home Care</h4><p>Professional cleaning with<br>unique cleaning guide</p></div><div class="svc-icon"><svg viewBox="0 0 44 44" fill="none" stroke="#3b4352" stroke-width="1.6"><path d="M8 22L22 10l14 12"/><path d="M12 20v14h20V20"/><path d="M18 34v-8h8v8"/></svg></div></div>
<div class="svc left" style="top:1693px"><div><h4>Safety &amp; Security</h4><p>Smart Lock<br>(Condo Compliant)</p></div><div class="svc-icon"><svg viewBox="0 0 44 44" fill="none" stroke="#3b4352" stroke-width="1.6"><rect x="10" y="20" width="18" height="16"/><path d="M14 20v-5a5 5 0 0110 0v5"/><circle cx="31" cy="14" r="6"/></svg></div></div>
<div class="svc right" style="top:1433px"><div class="svc-icon"><svg viewBox="0 0 44 44" fill="none" stroke="#3b4352" stroke-width="1.6"><rect x="14" y="8" width="22" height="16"/><circle cx="25" cy="16" r="4"/><path d="M8 30c6 0 8-4 14-4h8v4H20M8 36h22l8-8"/></svg></div><div><h4>Performance Optimiz...</h4><p>Proprietary Pricing Tool used<br>Only by Bright Door</p></div></div>
<div class="svc right" style="top:1563px"><div class="svc-icon"><svg viewBox="0 0 44 44" fill="none" stroke="#3b4352" stroke-width="1.6"><rect x="8" y="10" width="28" height="24"/><circle cx="22" cy="22" r="6"/><path d="M22 12v4M22 28v4M12 22h4M28 22h4"/></svg></div><div><h4>Safety &amp; Security</h4><p>We pro-actively monitor the<br>property through</p></div></div>
<div class="svc right" style="top:1693px"><div class="svc-icon"><svg viewBox="0 0 44 44" fill="none" stroke="#3b4352" stroke-width="1.6"><rect x="8" y="8" width="20" height="26"/><path d="M12 14h12M12 19h12M12 24h8"/><rect x="24" y="22" width="12" height="14"/><path d="M27 26h6M27 30h6"/></svg></div><div><h4>How is the management</h4><p>We strive to keep our fee as<br>simple as possible</p></div></div>
<div class="btn-outline">VIEW ALL SERVICE</div>

<svg class="fee-band" width="1200" height="610" viewBox="0 0 1200 610"><polygon points="0,0 1200,0 1200,610 0,460" fill="#4f7f8c"/></svg>
<div class="fee-strip"><span>BRIGHTDOOR</span></div>
<h2 class="fee-title">How is the management fee calculated</h2>
<div class="fee-text">
  <p>We strive to keep our fee as simple as possible with 80% of revenue going to you, 20% to Bright Door for the management and the cleaning fee is paid for by the guest.</p>
  <p style="margin-top:14px">For more information on our service options, please see our pricing area.</p>
</div>
<table class="fee-table">
  <tr><th>For<br>example</th><th></th><th>Nightly<br>Rate</th><th></th><th>Number of<br>Nights</th><th></th><th>Rental<br>Revenue</th><th></th></tr>
  <tr><td></td><td>Nightly<br>Revenue</td><td>$100</td><td>x</td><td>5</td><td>=</td><td>$500</td><td></td></tr>
  <tr><td></td><td>20% Bright<br>Door fee</td><td></td><td></td><td></td><td></td><td>$100</td><td></td></tr>
  <tr><td></td><td>Owner Net<br>Earnings</td><td></td><td></td><td></td><td></td><td>$400</td><td></td></tr>
</table>

<div class="photo" style="left:88px;top:2573px;width:552px;height:427px;clip-path:polygon(0 0,100% 0,68% 100%,0 100%)"><div role="img" aria-label="Bright living room with grey sofa and city view windows" style="background:linear-gradient(120deg,#c9cdd2 0%,#e6e8ea 45%,#9aa3ad 75%,#7d6a5c 100%)"></div></div>
<h2 class="block-title" style="left:672px;top:2655px;width:460px">What is a Short-Term Rental (STR)?</h2>
<div class="block-text" style="left:672px;top:2755px;width:440px">
  <p>A Short-Term Rental (STR) is a property that is typically rented for duration of less than 30-days. Although the property is rented for shorter durations (on average between 3-7 days), we would manage the property year-round. By renting on a shorter term, you are able to take advantage of peak demand periods throughout the year (Stampede, etc.) which results in a much higher revenue potential. With a significant amount of long-term rental inventory in Calgary, short-term rentals provide a solution to home owners and investor.</p>
</div>

<svg class="abs" style="left:555px;top:3053px" width="557" height="427" viewBox="0 0 557 427"><polygon points="40,0 70,0 30,427 0,427" fill="#4f7f8c"/></svg>
<div class="photo" style="left:575px;top:3053px;width:537px;height:427px;clip-path:polygon(14% 0,100% 0,100% 100%,0 100%)"><div role="img" aria-label="Condo interior with floor-to-ceiling windows and lounge chair" style="background:linear-gradient(100deg,#aeb8c4 0%,#dfe4ea 40%,#c3cad3 65%,#8c8f8e 100%)"></div></div>
<h2 class="block-title" style="left:88px;top:3165px;width:450px">Overview of BDRM</h2>
<div class="block-text" style="left:88px;top:3212px;width:430px;font-size:12.5px">
  <p>At Bright Door Rental Management, we manage the entire hosting process, so you don't have to.</p>
  <p>We do much more than provide a hassle-free experience, we specialize in maximizing the revenue from your property.</p>
  <p>As a Short-Term Rental (STR), your property is able to take advantage of peak rental demand periods which results in significantly greater revenue than a traditional rental property.</p>
</div>

<div class="pricing-bg"></div>
<h2 class="section-title" style="top:3645px">Our Pricing</h2>
<div class="price-card">
  <div class="price-side">
    <p class="lead-side" style="margin:0">Bright Door's share<br>of the nightly<br>revenue</p>
    <div class="big">20%</div>
    <p><strong>All money goes to your bank account,</strong> we invoice you one-time per month.</p>
    <p>There are <strong>no additional fees</strong> and best of all, <strong>no surprises!</strong></p>
  </div>
  <div class="price-main">
    <p class="lead">Our pricing structure is simple and easy to understand, that is by design!</p>
    <p>The nightly revenue is split between the Owner and Bright Door, 80% &amp; 20% respectively.</p>
    <p>The cleaning fee is paid for by the guest which covers all cleaning between guests. We do not take a fee from cleaning.</p>
    <span class="btn-dark">CLICK HERE TO SEE AN EXAMPLE</span>
  </div>
</div>

<h2 class="contact-title">Ready to get started or want more information?</h2>
<div class="field" style="left:625px;top:4283px;width:240px"><label>FIRST NAME</label><div class="box">Enter your name</div></div>
<div class="field" style="left:878px;top:4283px;width:240px"><label>LAST NAME</label><div class="box">Enter your last name</div></div>
<div class="field" style="left:625px;top:4366px;width:240px"><label>EMAIL*</label><div class="box">Enter your email</div></div>
<div class="field" style="left:843px;top:4366px;width:275px"><label>PHONE*</label><div class="box">Enter your number</div></div>
<div class="field" style="left:625px;top:4449px;width:493px"><label>MESSAGE*</label><div class="box" style="height:165px">Type your message</div></div>
<div class="btn-submit">SUBMIT NOW</div>

<svg class="footer-bg" width="1200" height="633" viewBox="0 0 1200 633"><polygon points="0,0 1200,40 1200,633 0,633" fill="#3b4352"/></svg>
<h2 class="news-title">Newsletter</h2>
<div class="news-form"><span class="mail"></span>Enter your email address<span class="go">SUBSCRIBE</span></div>

<div class="foot-brand">
  <span class="brand-mark" style="width:48px;height:48px"></span>
  <div><span class="brand-name">BrightDoor</span><span class="brand-sub">Rental Management</span></div>
</div>
<div class="social"><span></span><span></span><span></span></div>

<div class="foot-col" style="left:460px"><h5>Quick links</h5>Home<br>Our Pricing<br>Our Services<br>OurProperties<br>Contact Us</div>
<div class="foot-col" style="left:672px"><h5>Support</h5><div style="margin-top:8px">Terms of use<br>Terms and Conditions<br>Privacy Policy<br>Refunds.</div></div>
<div class="foot-col" style="left:890px;width:240px"><h5>Contact Us</h5>
  <div class="contact-row" style="margin-top:8px"><svg width="12" height="12" viewBox="0 0 12 12"><path d="M2 1l3 0 1 3-2 1a7 7 0 003 3l1-2 3 1v3c-6 0-9-3-9-9z" fill="#fff"/></svg>403-555-0147</div>
  <div class="contact-row"><svg width="12" height="10" viewBox="0 0 12 10"><rect width="12" height="10" fill="#fff"/><path d="M0 0l6 5 6-5" stroke="#3b4352" fill="none"/></svg>hello@brightdoorstays.ca</div>
  <div class="contact-row"><svg width="10" height="14" viewBox="0 0 10 14"><path d="M5 0a5 5 0 015 5c0 4-5 9-5 9S0 9 0 5a5 5 0 015-5z" fill="#fff"/><circle cx="5" cy="5" r="2" fill="#3b4352"/></svg>118 Lindell Row, Coral Bay,<br>FL 33100</div>
</div>

<p class="copy">© Copyright 2020 All Right Reserved</p>
<div class="chat"><svg width="22" height="20" viewBox="0 0 22 20"><path d="M11 1C5 1 1 4.5 1 9c0 2 1 4 3 5l-1 5 5-3c1 .3 2 .3 3 .3 6 0 10-3.5 10-8S17 1 11 1z" fill="#3b4352"/></svg></div>

</body>
</html>
```